Swimming Pool Supply Company Business Cards

We need business cards designed for company. These need to be easy to edit so that we can fill in names, titles, and contact info for each person who works here.

Dalton R. Whitfield
Manager of Legal & Finance
K.L. Brisbane, Incorporated

4837 Grenway Avenue
Marlow Heights, PA 19243

E. dalton@klbrisbane-example.com
M. (215) 555-0173
O. (215) 555-0148

Contact Information for Business Card

Looking to upgrade current business cards with graphic that can be edited. Looking for fresh ideas for an age old industry.

Font styles to use
Serif
Sans Serif

Colors

Designer to choose colors to be used in the design.

Requirements
Must have
• Professional, fresh, unique but professional

```html
<!DOCTYPE html>
<html lang="en">
<head>
<meta charset="utf-8">
<title>K.L. Brisbane Business Cards</title>
<link href="https://fonts.googleapis.com/css2?family=Montserrat:wght@400;500;600;700;800&display=swap" rel="stylesheet">
<style>
  :root {
    --backdrop: #d2d2d2;
    --card: #1e1f22;
    --ink-strong: #7a7a7c;
    --ink-soft: #8c8c8e;
    --ink-muted: #6a6a6c;
    --pill: #58585b;
    --pill-line: #7c7c7e;
    --ring: rgba(255,255,255,0.05);
  }
  * { box-sizing: border-box; margin: 0; padding: 0; }
  html, body { width: 1200px; height: 800px; overflow: hidden; }
  body {
    position: relative;
    background: var(--backdrop);
    font-family: "Montserrat", sans-serif;
  }
  .card {
    position: absolute;
    left: 340px;
    width: 520px;
    height: 297px;
    background: var(--card);
    overflow: hidden;
  }
  .card--front { top: 73px; }
  .card--back { top: 430px; }

  .texture {
    position: absolute;
    border-radius: 50%;
    background: radial-gradient(circle, var(--ring) 0%, rgba(255,255,255,0.025) 45%, rgba(255,255,255,0) 70%);
  }
  .card--front .texture { width: 420px; height: 420px; left: 50px; top: -50px; }
  .texture--corner { width: 300px; height: 300px; left: -150px; top: -150px; }
  .texture--side { width: 260px; height: 260px; left: 390px; top: 140px; }

  .wordmark {
    position: absolute;
    font-weight: 800;
    color: var(--ink-strong);
    text-transform: uppercase;
    letter-spacing: 1px;
    line-height: 1;
  }
  .card--front .wordmark {
    left: 0; right: 0; top: 122px;
    text-align: center;
    font-size: 50px;
  }
  .tagline {
    position: absolute;
    left: 0; right: 0; top: 177px;
    text-align: center;
    font-size: 10.5px;
    font-weight: 500;
    color: var(--ink-muted);
  }

  .identity {
    position: absolute;
    right: 90px; top: 16px;
    text-align: right;
    color: var(--ink-soft);
  }
  .identity__name { font-size: 19px; font-weight: 700; letter-spacing: 0.5px; }
  .identity__role, .identity__company { font-size: 10.5px; font-weight: 500; line-height: 13px; }

  .portrait-slot {
    position: absolute;
    left: 440px; top: 20px;
    width: 56px; height: 40px;
    background: #4a4a4d;
    border: 1px solid #6e6e70;
    transform: skewX(-20deg);
  }
  .portrait-slot__accent {
    position: absolute;
    left: 500px; top: 20px;
    width: 22px; height: 40px;
    background: #6a6a6c;
    transform: skewX(-20deg);
  }

  .card--back .wordmark { left: 38px; top: 184px; font-size: 29px; }

  .contact-rail {
    position: absolute;
    left: 218px; top: 121px;
    width: 28px; height: 156px;
    border-radius: 14px;
    background: var(--pill);
    border: 1px solid var(--pill-line);
  }
  .contact-rail__divider {
    position: absolute; left: 0; right: 0; height: 1px;
    background: var(--pill-line);
  }
  .contact-rail svg { position: absolute; left: 6px; width: 14px; height: 14px; }

  .contact-line {
    position: absolute;
    left: 254px;
    font-size: 12.5px;
    line-height: 15px;
    letter-spacing: 0.8px;
    color: var(--ink-soft);
  }
</style>
</head>
<body>

<section class="card card--front">
  <div class="texture" role="img" aria-label="Faint concentric ripple pattern"></div>
  <div class="wordmark">Brisbane</div>
  <p class="tagline">Big Enough To Serve You, Small Enough To Care</p>
</section>

<section class="card card--back">
  <div class="texture texture--corner" role="img" aria-label="Faint ripple pattern in corner"></div>
  <div class="texture texture--side" role="img" aria-label="Faint ripple pattern behind contacts"></div>

  <div class="identity">
    <p class="identity__name">Dalton R. Whitfield</p>
    <p class="identity__role">Manager of Legal &amp; Finance</p>
    <p class="identity__company">K.L. Brisbane, Incorporated</p>
  </div>
  <div class="portrait-slot" role="img" aria-label="Placeholder for staff portrait"></div>
  <div class="portrait-slot__accent"></div>

  <div class="wordmark">Brisbane</div>

  <div class="contact-rail">
    <svg style="top:11px" viewBox="0 0 24 24" fill="none" stroke="#2a2a2c" stroke-width="2"><path d="M5 3h4l2 5-3 2a12 12 0 0 0 6 6l2-3 5 2v4a2 2 0 0 1-2 2A17 17 0 0 1 3 5a2 2 0 0 1 2-2z"/></svg>
    <div class="contact-rail__divider" style="top:48px"></div>
    <svg style="top:70px" viewBox="0 0 24 24" fill="none" stroke="#2a2a2c" stroke-width="2"><rect x="3" y="5" width="18" height="14"/><path d="M3 5l9 8 9-8"/></svg>
    <div class="contact-rail__divider" style="top:106px"></div>
    <svg style="top:120px" viewBox="0 0 24 24" fill="#2a2a2c"><path d="M12 2a7 7 0 0 0-7 7c0 5 7 13 7 13s7-8 7-13a7 7 0 0 0-7-7zm0 9.5A2.5 2.5 0 1 1 12 6.5a2.5 2.5 0 0 1 0 5z"/></svg>
  </div>

  <p class="contact-line" style="top:130px">(215) 555-0173(M)<br>(215) 555-0148(O)</p>
  <p class="contact-line" style="top:191px">dalton@klbrisbane-example.com</p>
  <p class="contact-line" style="top:240px">4837 Grenway Avenue<br>Marlow Heights, PA 19243</p>
</section>

</body>
</html>
```